Real Estate Newsletter

I would like a template created for a monthly newsletter; ideally, two pages long, including my photo, logo and contact info. I need it to look professional and be very easy for me to drop text into.

Target Market(s)

Past/current clients

Industry/Entity Type

Real Estate Agent

Font styles to use
Serif

Requirements
Must have
• My contact info/photo and logo
• (206) 555-0187
• mkettridge@lunvoro.com
• www.MarlaKettridge.com
Nice to have
• I need a template where I can easily drop contact. I need the template to look professional so I can print it and mail it to current and past clients.

```html
<!DOCTYPE html>
<html lang="en">
<head>
<meta charset="utf-8">
<title>Marla Kettridge – Newsletter Template</title>
<link href="https://fonts.googleapis.com/css2?family=Open+Sans:wght@600;700;800&family=PT+Sans:wght@700&display=swap" rel="stylesheet">
<style>
  :root {
    --navy: #33439a;
    --band: #5c88c6;
    --ice: #d4ffff;
    --aqua-light: #8ffcff;
    --aqua: #1ef2ff;
    --block-top: #12eaf8;
    --block-bottom: #3bc2ee;
    --frame: rgba(255,255,255,0.4);
    --white: #ffffff;
    --photo-a: #8a6a55;
    --photo-b: #d8c8bc;
  }
  * { margin: 0; padding: 0; box-sizing: border-box; }
  html, body { width: 1200px; height: 1200px; overflow: hidden; background: var(--white); }
  body { position: relative; font-family: "Open Sans", Arial, sans-serif; }

  .page {
    position: absolute;
    width: 637px;
    overflow: hidden;
    background: linear-gradient(180deg, var(--aqua-light) 30%, var(--aqua) 100%);
  }
  .page--front { left: 22px; top: 181px; height: 766px; }
  .page--cover { left: 688px; top: 30px; height: 787px; transform: scale(0.75); transform-origin: 0 0; }

  .masthead-top { position: absolute; left: 0; top: 0; width: 100%; height: 110px; background: linear-gradient(180deg, var(--ice), #b4ffff); }
  .sidebar { position: absolute; left: 0; top: 0; width: 197px; height: 100%; background: var(--navy); }
  .title-band { position: absolute; left: 0; top: 110px; width: 100%; height: 137px; background: var(--band); }

  .agent-photo {
    position: absolute; left: 6px; top: 11px; width: 156px; height: 236px;
    background: linear-gradient(160deg, var(--photo-a) 0%, var(--photo-b) 60%, #3e4f70 100%);
  }

  .contact { position: absolute; left: 212px; top: 29px; color: var(--navy); font-weight: 700; font-size: 13px; line-height: 16px; }
  .brand { position: absolute; left: 422px; top: 56px; color: var(--navy); font-weight: 700; font-size: 21px; white-space: nowrap; }

  .title { position: absolute; left: 0; top: 110px; width: 637px; height: 137px; }
  .title text { font-family: "PT Sans", Arial, sans-serif; font-weight: 700; fill: var(--white); }

  .decor { position: absolute; left: 0; top: 0; width: 637px; height: 100%; }

  .lead { position: absolute; left: 212px; top: 254px; color: var(--navy); font-weight: 700; }
  .lead h2 { font-size: 19px; line-height: 22px; }
  .lead p { font-size: 12px; line-height: 14px; }

  .sidebar-text { position: absolute; left: 31px; color: var(--white); font-weight: 700; }
  .sidebar-text h3 { font-size: 21px; line-height: 26px; }
  .sidebar-text h4 { font-size: 15px; line-height: 20px; margin-top: 12px; }
  .sidebar-text p { font-size: 12.5px; line-height: 15.6px; margin-top: 14px; width: 160px; }
  .sidebar-text--one { top: 262px; }
  .sidebar-text--two { top: 487px; }

  .page--back {
    position: absolute; left: 537px; top: 660px; width: 405px; height: 502px; overflow: hidden;
    background: linear-gradient(180deg, #f4ffff 0%, #c8ffff 10%, var(--aqua-light) 45%, var(--aqua) 100%);
  }
  .page--back .brand { left: 271px; top: 34px; font-size: 14px; }
  .back-bar { position: absolute; left: 88px; top: 61px; width: 317px; height: 90px; background: var(--navy); }
  .back-block { position: absolute; left: 186px; top: 306px; width: 202px; height: 186px; background: linear-gradient(180deg, var(--block-top), var(--block-bottom)); }
</style>
</head>
<body>

  <section class="page page--front">
    <div class="masthead-top"></div>
    <svg class="decor" viewBox="0 0 637 766" aria-hidden="true">
      <defs>
        <linearGradient id="blockFill" x1="0" y1="0" x2="0" y2="1">
          <stop offset="0" stop-color="#12eaf8"/><stop offset="1" stop-color="#3bc2ee"/>
        </linearGradient>
      </defs>
      <rect x="292" y="459" width="318" height="280" fill="url(#blockFill)"/>
      <g fill="none" stroke="rgba(255,255,255,0.4)" stroke-width="9">
        <rect x="366" y="295" width="116" height="82"/>
        <rect x="432" y="321" width="133" height="117"/>
        <rect x="503" y="383" width="140" height="118"/>
        <rect x="224" y="674" width="133" height="110"/>
      </g>
    </svg>
    <div class="sidebar"></div>
    <div class="title-band"></div>
    <div class="agent-photo" role="img" aria-label="Portrait photo of the agent"></div>
    <div class="contact">
      <p>Contact Person</p>
      <p>- (206) 555-0187</p>
      <p>- mkettridge@lunvoro.com</p>
      <p>- www.MarlaKettridge.com</p>
    </div>
    <div class="brand">Marla Kettridge</div>
    <svg class="title" viewBox="0 0 637 137">
      <text x="186" y="58" font-size="46">The</text>
      <text x="112" y="122" font-size="116" textLength="518" lengthAdjust="spacingAndGlyphs">Newsletter</text>
    </svg>
    <div class="lead">
      <h2>sample text for use in news headlines</h2>
      <p>sample text for use in news headlines</p>
    </div>
    <div class="sidebar-text sidebar-text--one">
      <h3>text</h3>
      <h4>text</h4>
      <p>Example example example example example example example example example example example example example example example example</p>
    </div>
    <div class="sidebar-text sidebar-text--two">
      <h3>text</h3>
      <h4>text</h4>
      <p>Example example example example example example example example example example example example example example example example</p>
    </div>
  </section>

  <section class="page page--cover">
    <div class="masthead-top"></div>
    <svg class="decor" viewBox="0 0 637 787" aria-hidden="true">
      <defs>
        <linearGradient id="blockFill2" x1="0" y1="0" x2="0" y2="1">
          <stop offset="0" stop-color="#12eaf8"/><stop offset="1" stop-color="#3bc2ee"/>
        </linearGradient>
      </defs>
      <rect x="364" y="472" width="318" height="315" fill="url(#blockFill2)"/>
      <g fill="none" stroke="rgba(255,255,255,0.4)" stroke-width="9">
        <rect x="365" y="280" width="116" height="112"/>
        <rect x="428" y="332" width="133" height="132"/>
        <rect x="499" y="389" width="145" height="126"/>
        <rect x="222" y="688" width="133" height="110"/>
      </g>
    </svg>
    <div class="sidebar"></div>
    <div class="title-band"></div>
    <div class="agent-photo" role="img" aria-label="Portrait photo of the agent"></div>
    <div class="contact">
      <p>Contact Person</p>
      <p>- (206) 555-0187</p>
      <p>- mkettridge@lunvoro.com</p>
      <p>- www.MarlaKettridge.com</p>
    </div>
    <div class="brand">Marla Kettridge</div>
    <svg class="title" viewBox="0 0 637 137">
      <text x="186" y="58" font-size="46">The</text>
      <text x="112" y="122" font-size="116" textLength="518" lengthAdjust="spacingAndGlyphs">Newsletter</text>
    </svg>
  </section>

  <section class="page--back">
    <div class="brand">Marla Kettridge</div>
    <div class="back-bar"></div>
    <div class="back-block"></div>
  </section>

</body>
</html>
```